Road Construction Company needs business cards

We would like a new business card designed for our business.

We're a road construction company based in Qld, Australia.

Can the business card please have the following information on it.

Name: Brent Malvoy
Position: General Manager
Phone: 0471 592 304
Email: Brent.malvoy@quendix.com.au
Address: 87 Harrowgate Ave, Pindarra, QLD, 4000
Website: www.quendix.com.au

Visually we'd like the card to be professional and simple.

Attached is our logo.

Our website is www.quendix.com.au

Target Market(s)

Men aged 25-60

Contact Information for Business Card

As listed in project description

Font styles to use
Serif

Requirements
Must have
• Large logo on back of card

```html
<!DOCTYPE html>
<html lang="en">
<head>
<meta charset="utf-8">
<title>Quendix Road Construction – Business Card</title>
<link rel="stylesheet" href="https://fonts.googleapis.com/css2?family=Open+Sans:wght@400;600;700;800&display=swap">
<style>
  :root {
    --backdrop: #222327;
    --card-white: #ffffff;
    --brand-blue: #1456a5;
    --accent-blue: #42a9db;
    --ink: #111111;
    --shadow: rgba(0, 0, 0, 0.45);
  }
  * { margin: 0; padding: 0; box-sizing: border-box; }
  html, body {
    width: 1200px;
    height: 780px;
    overflow: hidden;
    background: var(--backdrop);
    font-family: "Open Sans", sans-serif;
  }
  .canvas {
    position: relative;
    width: 1200px;
    height: 780px;
    display: flex;
    align-items: center;
    justify-content: center;
    gap: 40px;
  }
  .card {
    position: relative;
    width: 540px;
    height: 310px;
    overflow: hidden;
    box-shadow: 0 10px 28px var(--shadow);
  }

  /* Back of card */
  .card-back {
    background: var(--brand-blue);
    display: flex;
    align-items: center;
    justify-content: center;
  }
  .card-back .brand-name {
    font-size: 82px;
    font-weight: 800;
    color: var(--card-white);
    letter-spacing: 2px;
    text-transform: uppercase;
  }

  /* Front of card */
  .card-front { background: var(--card-white); }
  .card-front .brand-name {
    position: absolute;
    top: 40px;
    right: 58px;
    font-size: 52px;
    font-weight: 800;
    color: var(--brand-blue);
    letter-spacing: 1.5px;
    text-transform: uppercase;
  }
  .identity-band {
    position: absolute;
    left: 0;
    top: 168px;
    width: 268px;
    height: 90px;
    background: var(--brand-blue);
    color: var(--card-white);
    display: flex;
    flex-direction: column;
    justify-content: center;
    align-items: flex-end;
    padding-right: 18px;
  }
  .person-name {
    font-size: 23px;
    font-weight: 700;
    text-transform: uppercase;
    letter-spacing: 0.5px;
    line-height: 1.1;
  }
  .person-role {
    font-size: 14px;
    font-weight: 600;
    letter-spacing: 0.6px;
  }
  .contact-band {
    position: absolute;
    left: 268px;
    top: 112px;
    right: 0;
    height: 80px;
    background: var(--accent-blue);
    color: var(--card-white);
    display: flex;
    flex-direction: column;
    justify-content: center;
    padding-left: 14px;
    gap: 2px;
  }
  .contact-line {
    display: flex;
    align-items: center;
    gap: 8px;
    font-size: 13px;
    font-weight: 400;
    letter-spacing: 0.4px;
  }
  .contact-icon { width: 12px; height: 12px; flex: none; }
  .address {
    position: absolute;
    left: 132px;
    top: 270px;
    font-size: 14px;
    color: var(--ink);
    letter-spacing: 0.4px;
  }
</style>
</head>
<body>
<main class="canvas">

  <section class="card card-back" aria-label="Business card back">
    <div class="brand-name">Quendix</div>
  </section>

  <section class="card card-front" aria-label="Business card front">
    <div class="brand-name">Quendix</div>

    <div class="contact-band">
      <div class="contact-line">
        <svg class="contact-icon" viewBox="0 0 24 24" aria-hidden="true"><path fill="currentColor" d="M6.6 10.8a15 15 0 0 0 6.6 6.6l2.2-2.2a1 1 0 0 1 1-.25 11.4 11.4 0 0 0 3.6.57 1 1 0 0 1 1 1V20a1 1 0 0 1-1 1A17 17 0 0 1 3 4a1 1 0 0 1 1-1h3.5a1 1 0 0 1 1 1c0 1.25.2 2.45.57 3.6a1 1 0 0 1-.25 1z"/></svg>
        <span>0471 592 304</span>
      </div>
      <div class="contact-line">
        <svg class="contact-icon" viewBox="0 0 24 24" aria-hidden="true"><circle cx="12" cy="12" r="9.5" fill="none" stroke="currentColor" stroke-width="2"/><path d="M2.5 12h19M12 2.5c3 3 3 16 0 19M12 2.5c-3 3-3 16 0 19" fill="none" stroke="currentColor" stroke-width="1.6"/></svg>
        <span>www.quendix.com.au</span>
      </div>
      <div class="contact-line">
        <svg class="contact-icon" viewBox="0 0 24 24" aria-hidden="true"><rect x="2" y="5" width="20" height="14" rx="1.5" fill="none" stroke="currentColor" stroke-width="2"/><path d="M3 6l9 7 9-7" fill="none" stroke="currentColor" stroke-width="2"/></svg>
        <span>Brent.malvoy@quendix.com.au</span>
      </div>
    </div>

    <div class="identity-band">
      <div class="person-name">Brent Malvoy</div>
      <div class="person-role">General Manager</div>
    </div>

    <p class="address">87 Harrowgate Ave, Pindarra, QLD, 4000</p>
  </section>

</main>
</body>
</html>
```